Meridian Growth Works (MGW)

Create a Flyer similar to the example or better

Target Market(s)

Management of Corporate Companies

Requirements
Must have
• follow the PDF-example
Nice to have
• compelling

```html
<!DOCTYPE html>
<html lang="en">
<head>
<meta charset="utf-8">
<title>Meridian Growth Works – Innovation Flyer</title>
<link href="https://fonts.googleapis.com/css2?family=Montserrat:wght@500;600&family=Raleway:wght@300;400&display=swap" rel="stylesheet">
<style>
  :root{
    --navy:#1b1f4b;
    --gold:#c9a33c;
    --gold-light:#e2c35a;
    --ink:#5a5d66;
    --paper:#ffffff;
    --mist:#f1f2f4;
    --sea-deep:#0f4a5a;
    --sea-light:#8fc3cc;
  }
  *{box-sizing:border-box;margin:0;padding:0}
  html,body{width:1200px;height:850px;overflow:hidden;background:var(--paper)}
  .flyer{position:relative;width:1200px;height:850px;overflow:hidden;font-family:'Raleway',sans-serif}
  .flyer-shapes{position:absolute;inset:0}
  .column{position:absolute;width:333px}
  .column h2{font-family:'Montserrat',sans-serif;font-weight:500;font-size:17.6px;line-height:21px;color:var(--navy);margin-bottom:28px}
  .column p{font-size:10.8px;line-height:13.9px;font-weight:300;color:var(--ink);text-align:justify;margin-bottom:13.9px}
  .col-origin{left:34px;top:313px}
  .col-disruption{left:431px;top:298px}
  .col-disruption h2{max-width:300px;margin-bottom:22px}
  .col-situation{left:827px;top:225px}
  .col-situation h2{margin-bottom:22px}
  .brand-badge{position:absolute;left:908px;top:22px;width:172px;height:172px;border-radius:50%;background:var(--navy);border:4px solid var(--paper);display:flex;align-items:center;justify-content:center;text-align:center;font-family:'Montserrat',sans-serif;font-weight:500;font-size:17px;line-height:22px;color:var(--paper)}
  .footer-name{position:absolute;left:828px;top:770px;font-family:'Montserrat',sans-serif;font-weight:600;font-size:14px;letter-spacing:2.4px;color:var(--gold-light)}
  .contact-list{position:absolute;left:828px;top:796px;width:340px;display:grid;grid-template-columns:auto auto 1fr;column-gap:14px;row-gap:6px;font-size:8.6px;line-height:11px;color:var(--paper)}
  .contact{display:flex;align-items:center;gap:4px;white-space:nowrap}
  .contact svg{width:10px;height:10px;flex:none}
  .contact-address{grid-column:1 / span 2}
  .contact-phone{justify-self:end;padding-left:14px}
  .contact-phone.no-icon{padding-left:28px}
  .copyright{position:absolute;left:475px;top:813px;font-size:10.5px;color:#d9dbe6}
</style>
</head>
<body>
<main class="flyer">
  <svg class="flyer-shapes" viewBox="0 0 1200 850" width="1200" height="850">
    <defs>
      <linearGradient id="goldBand" x1="0" y1="0" x2="1" y2="0">
        <stop offset="0" stop-color="#a88a2e"/>
        <stop offset="0.5" stop-color="#d9b64e"/>
        <stop offset="1" stop-color="#e6c65c"/>
      </linearGradient>
      <linearGradient id="sea" x1="0" y1="0" x2="1" y2="1">
        <stop offset="0" stop-color="#dfe9ea"/>
        <stop offset="0.35" stop-color="#8fc3cc"/>
        <stop offset="0.7" stop-color="#0f4a5a"/>
        <stop offset="1" stop-color="#2e7e86"/>
      </linearGradient>
      <linearGradient id="mistPanel" x1="0" y1="0" x2="1" y2="0">
        <stop offset="0" stop-color="#ffffff"/>
        <stop offset="1" stop-color="#f1f2f4"/>
      </linearGradient>
    </defs>
    <rect x="0" y="0" width="1200" height="310" fill="url(#goldBand)"/>
    <path role="img" aria-label="Photo: a surfer riding the face of a large breaking ocean wave" d="M0,0 L1000,0 C950,60 870,140 780,190 C650,252 520,240 420,238 C260,236 120,205 0,178 Z" fill="url(#sea)"/>
    <path d="M0,272 C150,282 300,285 400,280 C520,276 600,270 700,275 C740,277 770,282 790,286 C800,240 840,205 900,200 C1000,192 1100,210 1200,282 L1200,850 L0,850 Z" fill="var(--paper)"/>
    <rect x="405" y="276" width="385" height="500" fill="url(#mistPanel)"/>
    <rect x="790" y="290" width="30" height="480" fill="url(#mistPanel)" opacity="0.6"/>
    <path d="M0,754 C200,782 350,792 480,777 C600,762 700,752 780,737 C900,722 1050,720 1200,722 L1200,850 L0,850 Z" fill="var(--gold)"/>
    <path d="M0,762 C200,790 350,800 480,785 C600,770 700,760 780,745 C900,730 1050,728 1200,730 L1200,850 L0,850 Z" fill="var(--navy)"/>
  </svg>

  <div class="brand-badge">Meridian<br>Growth<br>Works</div>

  <section class="column col-origin">
    <h2>Innovation on Demand and where it originates…</h2>
    <p>The most valid and promising source of sustained innovation of your specific business will be found within your organization’s collective genius and creativity. Your organization has all necessary resources for the innovation of your business at hand. The problem is: These valuable resources are either engaged in the fulfilling of your corporate traditional business requirements or they are currently struggling with the integration of an “innovative” acquisition your corporate company has to handle.</p>
    <p>How might you access and leverage the inherent genius of your organization to develop new products and services for the era of “Disruptive Innovation”? The scale of Innovation your corporate business really demands will most recently not have taken place with the standard environment of the day-to-day business attitude. Innovation needs change, inspiration, and a conceptional thinking out of the box.</p>
    <p>Considering this, we have created a structured but nevertheless fully scalable and adjustable modular innovation process – Innovation results based on the principals of the “Theory U” by C. O. Halvorsen, Design Thinking (Northloop), Neurolinguistic Programming (NLP) and some other Agile and other SCRUM methodologies more. The complete process will be executed by the experts in your organization during (max.) 5 days, in our pre-configured agile innovation facility located and ready to use on a country estate in Italy.</p>
  </section>

  <section class="column col-disruption">
    <h2>Disruptive Innovation and what it means for your corporate business…</h2>
    <p>As a striking example, let us briefly look at the fact and the consequence of “Disruptive Innovation” in the area of “Diabetes Care Products”. Imagine – you are the owner of a production site of let’s say “Diabetes Products” for which you have to implement a huge number of regulations and processes – all the while, additionally having to facilitate a remarkable value of assets, to produce products you will need for the fulfilling of your customer’s needs.</p>
    <p>The corporate thinking of your organization runs on the fact of keeping your business alive, vital, and productive. You will most recently have not become aware of the fact that one huge organization, being totally out of the scope of your competitor analyses, is currently inventing a device which makes 90 percent of your products and services obsolete. And if this fact is not astonishing enough, here is one more remarkable fact: A tiny little organization and newly established business in the US, is currently developing and certifying a substituting remedy for the Diabetes disease you have been creating your revenue with, over decades.</p>
    <p>And here comes the burning question to the innovation capacity of your corporate organization: How come all your experts and all your organization’s expertise was not able to foresee nor to anticipate this fact of “Disruptive Innovation” of approximately 90 percent of your corporate business? How come the rights and patents are not one of your organization’s assets?</p>
  </section>

  <section class="column col-situation">
    <h2>The Current Situation all “corporate businesses” are currently facing…</h2>
    <p>How your corporate business will be enabled to succeed in the era of “Disruptive Innovation”?</p>
    <p>Here is the fact: Your corporate business is designed to stay in compliance with demanding regulations and it has to obey to rules of the processes. GxP, HRA and GRC and numberless additional business specific regulations and requirements are representing a framework of major influencers enabling and supporting the success of your established business and go-to-market models.</p>
    <p>We totally agree: Compliance and regulations are key to operating a successful corporate business organization. However, on the other hand, there are these regulations slowing down, hindering or even disabling your capacity to innovate within the era of “Disruptive Innovation”. If we talk about “Disruptive Innovation”, we mean exactly that: Disruption - of traditional collaboration attitudes and unchanged continuation of corporate business organizations. In our era, corporate organizations of all kinds need more than just elaborating around the symptoms and trying to handle them by simple implementation attempts of new IT-Infrastructures – corporate businesses need desperately a true and honest reflection upon the existing facts and in the consequence, they have to come up with valid answers to the profound challenges of the drastically changing business challenges ahead.</p>
    <p>How can you expect your corporate organization to innovate on products, processes or global synergetic collaboration, if your people and your organization are 100 percent engaged in fulfilling and ensuring the functioning of given requirements in the context of your corporate business?</p>
  </section>

  <div class="footer-name">Meridian Growth Works LLC</div>

  <address class="contact-list" style="font-style:normal">
    <div class="contact contact-address">
      <svg viewBox="0 0 10 10"><path d="M5,0.5 C2.8,0.5 1.5,2 1.5,3.8 C1.5,6.3 5,9.5 5,9.5 C5,9.5 8.5,6.3 8.5,3.8 C8.5,2 7.2,0.5 5,0.5 Z" fill="#fff"/><circle cx="5" cy="3.8" r="1.3" fill="#1b1f4b"/></svg>
      Seeuferweg 22 CH – 6000 Lakeside / LU
    </div>
    <div class="contact contact-phone">
      <svg viewBox="0 0 10 10"><path d="M2.2,0.6 L3.8,2.8 L2.9,4 C3.6,5.5 4.6,6.5 6,7.1 L7.2,6.2 L9.4,7.8 L8.4,9.4 C4.4,9.2 0.8,5.6 0.6,1.6 Z" fill="#fff"/></svg>
      +41 41 555 01 20
    </div>
    <div class="contact">
      <svg viewBox="0 0 10 10" fill="none" stroke="#fff" stroke-width="0.9"><circle cx="5" cy="5" r="4.2"/><ellipse cx="5" cy="5" rx="1.8" ry="4.2"/><path d="M0.8,5 H9.2 M1.6,2.8 H8.4 M1.6,7.2 H8.4"/></svg>
      www.MGWorks.ch
    </div>
    <div class="contact">
      <svg viewBox="0 0 10 10"><rect x="0.5" y="2" width="9" height="6.5" fill="#fff"/><path d="M0.8,2.3 L5,5.8 L9.2,2.3" fill="none" stroke="#1b1f4b" stroke-width="0.9"/></svg>
      office@mgworks.ch
    </div>
    <div class="contact contact-phone no-icon">+41 79 555 0147</div>
  </address>

  <div class="copyright">Copyright Meridian Growth Works LLC</div>
</main>
</body>
</html>
```